依頼詳細
会社の名刺を新しくしたいと思っております。移転予定がありますので、フォントに関してはイラストレーターCS6に入っているものでアウトラインへ変更なしでお願いします。
記載項目
表面:ロゴ、会社名、会社住所、役職、名前、電話番号、ファックス番号、携帯番号、メール、HP
裏面:事業内容(販売事業、ロジスティック事業、生産事業、エネルギー事業)、店舗ロゴ(風見屋)、営業所
希望イメージ
シンプル 複雑
単色 カラフル
暗い 明るい
日常 高級
遊び心 厳粛
未来的 伝統的
女性的 男性的
希望する色
茶系、黄・オレンジ系
納品ファイル
• イラストレーター形式 (.ai)
補足説明
現在、使用している名刺とロゴを追加します。
名刺裏面の風見屋ロゴを追加致します。

サンプルで提示した名刺裏面の事業内容ですが、細かい内容は省いて頂いて結構です。

宜しくお願い致します。
お世話になっております。

ご要望と致しましては、シンプルでスタイリッシュな名刺を希望しております。
裏面ですが、事業内容は4つの記載だけで添付ファイルのように、細かい記載は省いていただいて結構です。
内容は下記をご参照ください。

上記の記載でお願い致します。

名刺に関しましては横型・縦型どちらでも構いません。

宜しくお願い致します。

シンプルで印象に残りましたので選ばして頂きました。
ありがとうございました。

たくさんのご提案ありがとうございました。

```html
<!DOCTYPE html>
<html lang="ja">
<head>
<meta charset="utf-8">
<title>株式会社SORANO 名刺</title>
<link rel="stylesheet" href="https://fonts.googleapis.com/css2?family=Noto+Sans+JP:wght@400;500;700&family=Montserrat:wght@500;700&display=swap">
<style>
  :root {
    --page: #eeeeec;
    --card: #ffffff;
    --brown: #5b3b22;
    --text: #3d3128;
    --muted: #777777;
    --orange: #e8891c;
    --line: #d9c3a0;
    --tint: rgba(236, 225, 205, 0.45);
  }
  * { margin: 0; padding: 0; box-sizing: border-box; }
  html, body { width: 812px; height: 1200px; overflow: hidden; background: var(--page); }
  body { font-family: "Noto Sans JP", sans-serif; color: var(--text); position: relative; }
  .card {
    position: absolute; left: 36px; width: 740px; height: 520px;
    background: var(--card); overflow: hidden;
    box-shadow: 0 2px 6px rgba(0,0,0,.12);
  }
  .card--front { top: 40px; }
  .card--back { top: 620px; }
  .texture { position: absolute; inset: 0; }
  .card--front .texture {
    background:
      radial-gradient(circle at 85% 30%, var(--tint) 0, transparent 55%),
      radial-gradient(circle at 30% 100%, var(--tint) 0, transparent 40%);
  }
  .card--back .texture {
    background:
      radial-gradient(circle at 15% 10%, var(--tint) 0, transparent 45%),
      radial-gradient(circle at 85% 80%, var(--tint) 0, transparent 50%);
  }
  .abs { position: absolute; white-space: nowrap; }

  .title { left: 36px; top: 24px; font-size: 16px; }
  .person-name { left: 34px; top: 50px; font-size: 38px; font-weight: 500; letter-spacing: 4px; }
  .person-roman { left: 36px; top: 106px; font-size: 14px; color: var(--muted); }
  .divider-v { left: 318px; top: 0; width: 1.5px; height: 200px; background: var(--line); }

  .company { left: 336px; top: 24px; font-size: 18px; font-weight: 500; }
  .contact { left: 336px; font-size: 14px; display: flex; align-items: center; gap: 6px; }
  .contact svg { width: 17px; height: 17px; fill: var(--brown); flex: none; }
  .contact .gap { width: 14px; }
  .contact--addr { top: 58px; }
  .contact--tel { top: 86px; }
  .contact--mob { top: 114px; }
  .divider-h { left: 330px; top: 148px; width: 390px; height: 1.5px; background: var(--line); }

  .brand-name { left: 34px; top: 372px; font-family: "Montserrat", sans-serif; font-weight: 700; font-size: 60px; letter-spacing: 2px; color: var(--brown); }
  .site { right: 34px; top: 442px; font-family: "Montserrat", sans-serif; font-weight: 500; font-size: 20px; color: var(--text); }

  .business-list { position: absolute; left: 40px; top: 46px; list-style: none; }
  .business-list li { font-size: 24px; line-height: 40px; display: flex; align-items: center; gap: 12px; }
  .business-list li::before { content: ""; width: 16px; height: 16px; background: var(--orange); }

  .shop { left: 540px; top: 160px; display: flex; align-items: center; gap: 10px; }
  .shop-mark { width: 26px; height: 26px; background: var(--brown); }
  .shop-name { font-size: 36px; font-weight: 700; color: var(--brown); letter-spacing: 2px; }

  .office-name { left: 36px; top: 336px; font-size: 18px; font-weight: 500; }
  .office-addr { top: 372px; left: 36px; }
  .office-tel { top: 400px; left: 36px; }
</style>
</head>
<body>

<section class="card card--front">
  <div class="texture" role="img" aria-label="淡いベージュの円形背景模様"></div>

  <p class="abs title">代表取締役</p>
  <p class="abs person-name">森本 千晴</p>
  <p class="abs person-roman">chiharu morimoto</p>
  <div class="abs divider-v"></div>

  <p class="abs company">株式会社SORANO</p>
  <p class="abs contact contact--addr">
    <svg viewBox="0 0 24 24"><path d="M12 2a7 7 0 0 0-7 7c0 5 7 13 7 13s7-8 7-13a7 7 0 0 0-7-7zm0 9.5A2.5 2.5 0 1 1 12 6.5a2.5 2.5 0 0 1 0 5z"/></svg>
    〒800-0000 架空県みどり市桜ヶ丘町1-2-3
  </p>
  <p class="abs contact contact--tel">
    <svg viewBox="0 0 24 24"><path d="M6.6 10.8a15 15 0 0 0 6.6 6.6l2.2-2.2a1 1 0 0 1 1-.25 11 11 0 0 0 3.6.6 1 1 0 0 1 1 1V20a1 1 0 0 1-1 1A17 17 0 0 1 3 4a1 1 0 0 1 1-1h3.5a1 1 0 0 1 1 1 11 11 0 0 0 .6 3.6 1 1 0 0 1-.25 1z"/></svg>
    0000-00-1234
    <span class="gap"></span>
    <svg viewBox="0 0 24 24"><path d="M6 2h9l3 3v5H6zM3 10h18v10H3zm4 3v2h4v-2zm0 4v1h4v-1zm9-4a1.5 1.5 0 1 0 0 3 1.5 1.5 0 0 0 0-3z"/></svg>
    0000-00-1235
  </p>
  <p class="abs contact contact--mob">
    <svg viewBox="0 0 24 24"><path d="M7 1h10a2 2 0 0 1 2 2v18a2 2 0 0 1-2 2H7a2 2 0 0 1-2-2V3a2 2 0 0 1 2-2zm0 3v14h10V4zm5 15.5a1 1 0 1 0 0 2 1 1 0 0 0 0-2z"/></svg>
    090-0000-0000
    <span class="gap"></span>
    <svg viewBox="0 0 24 24"><path d="M2 5h20v14H2zm2 2v.5l8 5.5 8-5.5V7zm0 2.9V17h16V9.9l-8 5.5z"/></svg>
    info@sorano-kyushu.com
  </p>
  <div class="abs divider-h"></div>

  <p class="abs brand-name">SORANO</p>
  <p class="abs site">www.sorano-kyushu.com</p>
</section>

<section class="card card--back">
  <div class="texture" role="img" aria-label="淡いベージュの円形背景模様"></div>

  <ul class="business-list">
    <li>販売事業</li>
    <li>ロジスティック事業</li>
    <li>生産事業</li>
    <li>エネルギー事業</li>
  </ul>

  <div class="abs shop">
    <span class="shop-mark"></span>
    <span class="shop-name">風見屋</span>
  </div>

  <p class="abs office-name">株式会社SORANO 桜川営業所</p>
  <p class="abs contact office-addr">
    <svg viewBox="0 0 24 24"><path d="M12 2a7 7 0 0 0-7 7c0 5 7 13 7 13s7-8 7-13a7 7 0 0 0-7-7zm0 9.5A2.5 2.5 0 1 1 12 6.5a2.5 2.5 0 0 1 0 5z"/></svg>
    〒800-0001 架空県みどり郡桜川町大字上野12-3
  </p>
  <p class="abs contact office-tel">
    <svg viewBox="0 0 24 24"><path d="M6.6 10.8a15 15 0 0 0 6.6 6.6l2.2-2.2a1 1 0 0 1 1-.25 11 11 0 0 0 3.6.6 1 1 0 0 1 1 1V20a1 1 0 0 1-1 1A17 17 0 0 1 3 4a1 1 0 0 1 1-1h3.5a1 1 0 0 1 1 1 11 11 0 0 0 .6 3.6 1 1 0 0 1-.25 1z"/></svg>
    0000-11-2345
  </p>
</section>

</body>
</html>
```